Flyer for the Harvest Lantern Gathering 2018

Design a flyer for our annual conference with basic information about the conference: conference logo and year,

Location:
Tolvane Community Center (Downtown Portland)
482 Wexmoor Street, Portland, ME 04107,

Date:
August 24th, 25th and 26th, 2018
Start time 6:00PM

I would like the following three words added to the flyer. These words describe the vision of the conference:
Prophetic, Worship, Prayer

```html
<!DOCTYPE html>
<html lang="en">
<head>
<meta charset="utf-8">
<title>Harvest Lantern Gathering 2018 — Flyer</title>
<link rel="stylesheet" href="https://fonts.googleapis.com/css2?family=Exo+2:wght@800;900&family=Lato:wght@700;900&display=swap">
<style>
  :root {
    --red: #e8302a;
    --orange: #f26a1e;
    --amber: #f7a21b;
    --yellow: #fbd129;
    --ink: #1b1b1b;
    --label: #f26522;
    --paper: #ffffff;
    --shadow: #c9c9c9;
  }
  * { margin: 0; padding: 0; box-sizing: border-box; }
  html, body { width: 1200px; height: 848px; overflow: hidden; background: var(--paper); }
  .flyer {
    position: relative;
    width: 1200px;
    height: 848px;
    overflow: hidden;
    background: var(--paper);
    font-family: "Lato", sans-serif;
  }
  .backdrop { position: absolute; inset: 0; }
  .vision-band {
    position: absolute;
    top: 0; left: 0; width: 100%; height: 92px;
    background: linear-gradient(90deg, var(--red) 0%, #ec4a25 60%, #f0652a 100%);
    display: flex; align-items: center;
    padding-left: 62px;
    font-family: "Exo 2", sans-serif;
    font-weight: 900;
    font-size: 50px;
    letter-spacing: 1px;
    color: var(--paper);
    text-transform: uppercase;
  }
  .vision-band .divider { margin: 0 14px; font-weight: 800; }
  .title {
    position: absolute;
    left: 58px; top: 108px;
    font-family: "Exo 2", sans-serif;
    font-weight: 900;
    color: var(--ink);
    text-transform: uppercase;
    line-height: 0.92;
  }
  .title .line-one { font-size: 100px; letter-spacing: 1px; }
  .title .line-two { font-size: 144px; letter-spacing: 2px; }
  .title .line-three { display: flex; align-items: flex-end; font-size: 88px; letter-spacing: 1px; }
  .title .year { font-size: 44px; margin-left: 16px; margin-bottom: 10px; }
  .brand {
    position: absolute;
    right: 60px; top: 470px;
    display: flex; align-items: center; gap: 18px;
  }
  .brand .mark {
    width: 92px; height: 92px; border-radius: 50%;
    border: 5px solid var(--amber);
  }
  .brand .name {
    font-family: "Exo 2", sans-serif;
    font-weight: 800;
    font-size: 58px;
    letter-spacing: 2px;
    color: var(--ink);
  }
  .details {
    position: absolute;
    left: 62px; bottom: 40px;
    color: var(--ink);
    font-weight: 900;
    font-size: 26px;
    line-height: 1.2;
  }
  .details .label {
    font-family: "Exo 2", sans-serif;
    font-weight: 900;
    color: var(--label);
    font-size: 38px;
    text-transform: uppercase;
    line-height: 1.05;
  }
  .details .block + .block { margin-top: 10px; }
</style>
</head>
<body>
  <main class="flyer">
    <svg class="backdrop" width="1200" height="848" viewBox="0 0 1200 848" aria-hidden="true">
      <defs>
        <linearGradient id="heat" x1="0" y1="1" x2="1" y2="0">
          <stop offset="0" stop-color="#ee4a24"/>
          <stop offset="0.45" stop-color="#f47c1e"/>
          <stop offset="1" stop-color="#fbc21f"/>
        </linearGradient>
        <radialGradient id="glow" cx="0.78" cy="0.35" r="0.45">
          <stop offset="0" stop-color="#fde25a" stop-opacity="0.9"/>
          <stop offset="1" stop-color="#fde25a" stop-opacity="0"/>
        </radialGradient>
      </defs>
      <rect class="heat-field" x="0" y="0" width="1200" height="848" fill="url(#heat)"/>
      <rect class="heat-glow" x="0" y="0" width="1200" height="848" fill="url(#glow)"/>
      <path class="wave-shadow" d="M0,492 C250,442 520,532 760,452 C940,392 960,302 1200,282 L1200,848 L0,848 Z" fill="var(--shadow)"/>
      <path class="wave-paper" d="M0,518 C250,468 520,558 760,478 C940,418 960,328 1200,308 L1200,848 L0,848 Z" fill="var(--paper)"/>
    </svg>

    <div class="vision-band">
      <span>Prophetic</span><span class="divider">|</span><span>Worship</span><span class="divider">|</span><span>Prayer</span>
    </div>

    <h1 class="title">
      <div class="line-one">Harvest</div>
      <div class="line-two">Lantern</div>
      <div class="line-three"><span>Gathering</span><span class="year">2018</span></div>
    </h1>

    <div class="brand">
      <span class="mark"></span>
      <span class="name">HLGCON</span>
    </div>

    <section class="details">
      <div class="block">
        <div class="label">Location:</div>
        <div>Tolvane Community Center (Downtown Portland)</div>
        <div>482 Wexmoor Street, Portland, ME 04107</div>
      </div>
      <div class="block">
        <div class="label">Date:</div>
        <div>August 24th, 25th &amp; 26th, 2018</div>
        <div>Start time 6:00PM</div>
      </div>
    </section>
  </main>
</body>
</html>
```